Online Travel Agency card design with 2 logos

Need a two sided business card design for online tourism agency which is based in Istanbul Turkey.
Need a business card design where it shows the travel agency logo but also the logo and information of the parent company as well.Parent company logo is just text with 2 different colors. (Arial font with text ToreVextra "Tore"- hex #172841 and "Vextra" hex-#FF7F00)
Both logos are uploaded.
Target Market(s)
travel , online
Industry/Entity Type
Travel
Contact Information for Business Card
The information on the card should be as :
Travel Agency Logo logo (pnlogo)
Parent Company logo(torelogo)
Company information :ToreVextra Turizm ve Bilgi Teknolojileri A.Ş
Address of company
Tel
Email
Name
Position(english and turkish)

```html
<!DOCTYPE html>
<html lang="en">
<head>
<meta charset="utf-8">
<title>ToreVextra Business Card</title>
<link rel="stylesheet" href="https://fonts.googleapis.com/css2?family=Open+Sans:wght@600&family=Titillium+Web:wght@400;600&family=Crimson+Text:ital@1&display=swap">
<style>
  :root {
    --navy: #2e3370;
    --orange: #f28a30;
    --orange-deep: #f07f22;
    --white: #ffffff;
    --paper: #e6e6e6;
    --ink: #2e3370;
  }
  * { margin: 0; padding: 0; box-sizing: border-box; }
  html, body { width: 1200px; height: 1200px; overflow: hidden; }
  body { background: var(--paper); position: relative; }

  .card {
    position: absolute;
    width: 680px;
    height: 440px;
    background: var(--white);
    overflow: hidden;
  }
  .card--back { left: 445px; top: 88px; display: flex; align-items: center; justify-content: center; }
  .card--front { left: 80px; top: 586px; }

  .wordmark {
    font-family: "Open Sans", Arial, sans-serif;
    font-weight: 600;
    color: var(--navy);
    letter-spacing: -0.5px;
  }
  .card--back .wordmark { font-size: 80px; }
  .card--front .wordmark { position: absolute; left: 18px; top: 54px; font-size: 45px; }

  .card__shape { position: absolute; inset: 0; }

  .company {
    position: absolute;
    left: 18px;
    top: 346px;
    font-family: "Crimson Text", Georgia, serif;
    font-style: italic;
    font-size: 22px;
    line-height: 34px;
    color: var(--ink);
  }

  .contact {
    position: absolute;
    font-family: "Titillium Web", Arial, sans-serif;
    font-weight: 600;
    color: var(--white);
    font-size: 20px;
    white-space: nowrap;
  }
  .contact--name { left: 355px; top: 48px; font-size: 33px; font-weight: 400; }
  .contact--name .role { font-size: 20px; font-weight: 600; }
  .contact--phone { left: 318px; top: 146px; }
  .contact--email { left: 320px; top: 226px; }
  .contact--web { left: 330px; top: 305px; }
  .contact--address { left: 362px; top: 383px; }
</style>
</head>
<body>

<section class="card card--back">
  <div class="wordmark">ToreVextra</div>
</section>

<section class="card card--front">
  <svg class="card__shape" width="680" height="440" viewBox="0 0 680 440">
    <defs>
      <linearGradient id="orangeFill" x1="0" y1="0" x2="0" y2="1">
        <stop offset="0" stop-color="#f3913c"/>
        <stop offset="1" stop-color="#f07f22"/>
      </linearGradient>
    </defs>
    <path d="M358,0 C278,120 262,300 342,440" fill="none" stroke="#2e3370" stroke-width="4"/>
    <path d="M370,0 C290,120 274,300 354,440 L680,440 L680,0 Z" fill="url(#orangeFill)"/>

    <g class="icon" transform="translate(316,66)">
      <circle r="24" fill="var(--orange)" stroke="#fff" stroke-width="3"/>
      <circle cy="-6" r="6" fill="#fff"/>
      <path d="M-11,12 C-11,2 11,2 11,12 Z" fill="#fff"/>
    </g>
    <g class="icon" transform="translate(282,154)">
      <circle r="24" fill="var(--orange)" stroke="#fff" stroke-width="3"/>
      <path d="M-12,-4 C-12,-12 12,-12 12,-4 L7,-4 L7,-7 L-7,-7 L-7,-4 Z" fill="#fff"/>
      <path d="M-8,-2 L8,-2 L11,10 L-11,10 Z" fill="#fff"/>
      <circle cy="4" r="3.5" fill="var(--orange)"/>
    </g>
    <g class="icon" transform="translate(278,242)">
      <circle r="24" fill="var(--orange)" stroke="#fff" stroke-width="3"/>
      <rect x="-11" y="-7" width="22" height="15" fill="#fff"/>
      <polyline points="-11,-7 0,2 11,-7" fill="none" stroke="var(--orange)" stroke-width="2"/>
    </g>
    <g class="icon" transform="translate(293,324)">
      <circle r="24" fill="var(--orange)" stroke="#fff" stroke-width="3"/>
      <circle r="11" fill="none" stroke="#fff" stroke-width="2"/>
      <ellipse rx="5" ry="11" fill="none" stroke="#fff" stroke-width="1.6"/>
      <line x1="-11" y1="0" x2="11" y2="0" stroke="#fff" stroke-width="1.6"/>
    </g>
    <g class="icon" transform="translate(323,402)">
      <circle r="24" fill="var(--orange)" stroke="#fff" stroke-width="3"/>
      <polygon points="0,-11 -12,0 -8,0 -8,10 8,10 8,0 12,0" fill="#fff"/>
      <rect x="-3" y="3" width="6" height="7" fill="var(--orange)"/>
    </g>
  </svg>

  <div class="wordmark">ToreVextra</div>

  <p class="company">ToreVextra Turizm<br>Ve Bilgi Teknolojileri A.Ş</p>

  <p class="contact contact--name">SELIM ARKAN | <span class="role">Director</span></p>
  <p class="contact contact--phone">+90-212-555-0183</p>
  <p class="contact contact--email">selim@torevextra.com</p>
  <p class="contact contact--web">www.torevextra.com</p>
  <p class="contact contact--address">Sample city, Sample country Land</p>
</section>

</body>
</html>
```